Business Card and Letterhead for Nurlo - modern real estate business

I need a double sided business card design for Nurlo. Please see business card brief here https://papers.trelvimo.net/sheet/q/7XrTbaLeZpMmQ2uWvd9HkCj4yNoEfsGi3lRtAz_pk/view?mode=shared

Please feel free to design the business cards however you feel best. I am happy to give some creative freedoms and then provide feedback from there.

Please then also create a letterhead to match the business card design

Colors

Designer to choose colors to be used in the design.

Requirements
Must have
• Must be a modern, elegant business card which looks very professional

```html
<!DOCTYPE html>
<html lang="en">
<head>
<meta charset="utf-8">
<title>Nurlo – Business Card</title>
<link rel="stylesheet" href="https://fonts.googleapis.com/css2?family=Raleway:wght@300;400;600;700&display=swap">
<style>
  :root {
    --stage: #6a6a6a;
    --card-black: #050505;
    --brand-red: #b0060c;
    --logo-red: #c4111a;
    --white: #ffffff;
    --soft-white: #f1e3e3;
    --photo-sky: #9fb4c9;
    --photo-green: #4f6a3c;
    --photo-olive: #8a8b4a;
  }
  * { box-sizing: border-box; margin: 0; padding: 0; }
  html, body { width: 1200px; height: 791px; overflow: hidden; }
  body {
    background: var(--stage);
    font-family: "Raleway", sans-serif;
    position: relative;
  }
  .card {
    position: absolute;
    top: 125px;
    width: 330px;
    height: 540px;
    overflow: hidden;
    box-shadow: 0 18px 40px rgba(0,0,0,0.35);
  }
  .card-back { left: 215px; background: var(--card-black); }
  .card-front { left: 655px; background: var(--brand-red); }

  .wordmark {
    color: var(--logo-red);
    font-weight: 600;
    font-size: 38px;
    letter-spacing: 4px;
    text-align: center;
  }
  .card-back .wordmark {
    position: absolute;
    top: 230px; left: 0; right: 0;
  }
  .web {
    position: absolute;
    bottom: 44px; left: 0; right: 0;
    text-align: center;
    color: var(--white);
    font-size: 14px;
    letter-spacing: 1px;
  }
  .web svg { display: block; margin: 0 auto 10px; }

  .portrait-area {
    position: absolute;
    top: 0; left: 0; right: 0;
    height: 135px;
    background: linear-gradient(160deg, var(--photo-sky) 0%, var(--photo-green) 55%, var(--photo-olive) 100%);
  }
  .profile {
    position: absolute;
    top: 160px; left: 34px; right: 24px;
    color: var(--white);
  }
  .profile .name { font-size: 27px; font-weight: 700; }
  .profile .role { font-size: 14px; font-weight: 300; color: var(--soft-white); margin-top: 6px; }
  .contacts {
    list-style: none;
    position: absolute;
    top: 250px; left: 34px;
    color: var(--white);
    font-size: 13.5px;
    letter-spacing: 0.5px;
  }
  .contacts li { display: flex; align-items: flex-start; gap: 14px; margin-bottom: 14px; line-height: 1.45; }
  .contacts svg { flex: none; margin-top: 2px; }
  .footer-block {
    position: absolute;
    left: 0; right: 0; bottom: 0;
    height: 160px;
  }
  .footer-block svg.shape { position: absolute; inset: 0; }
  .footer-block .wordmark {
    position: absolute;
    top: 66px; left: 0; right: 0;
  }
</style>
</head>
<body>

<section class="card card-back">
  <div class="wordmark">NURLO</div>
  <div class="web">
    <svg width="16" height="16" viewBox="0 0 16 16" fill="none" stroke="#c4111a" stroke-width="1.4">
      <circle cx="8" cy="8" r="6.5"/>
      <ellipse cx="8" cy="8" rx="3" ry="6.5"/>
      <line x1="1.5" y1="8" x2="14.5" y2="8"/>
    </svg>
    www.nurlo.com
  </div>
</section>

<section class="card card-front">
  <div class="portrait-area" role="img" aria-label="Portrait photo of the agent outdoors with trees and a valley view"></div>
  <div class="profile">
    <div class="name">Liam Carter</div>
    <div class="role">Licenced Real Estate Agent</div>
  </div>
  <ul class="contacts">
    <li>
      <svg width="14" height="14" viewBox="0 0 24 24" fill="#fff"><path d="M6.6 10.8a15.1 15.1 0 0 0 6.6 6.6l2.2-2.2c.3-.3.7-.4 1-.2 1.1.4 2.3.6 3.6.6.6 0 1 .4 1 1V20c0 .6-.4 1-1 1A17 17 0 0 1 3 4c0-.6.4-1 1-1h3.5c.6 0 1 .4 1 1 0 1.3.2 2.5.6 3.6.1.3 0 .7-.2 1z"/></svg>
      <span>0491 570 156</span>
    </li>
    <li>
      <svg width="14" height="14" viewBox="0 0 24 24" fill="#fff"><path d="M2 5h20v14H2z M2 5l10 8 10-8" /><path d="M3 6l9 7 9-7" fill="none" stroke="#b0060c" stroke-width="2"/></svg>
      <span>liam@nurlo.com</span>
    </li>
    <li>
      <svg width="14" height="16" viewBox="0 0 24 28" fill="#fff"><rect x="4" y="2" width="2.5" height="24"/><path d="M6.5 3h14l-4 5 4 5h-14z"/></svg>
      <span>PO Box 3162<br>Ashvale NSW 2790</span>
    </li>
  </ul>
  <div class="footer-block">
    <svg class="shape" width="330" height="160" viewBox="0 0 330 160">
      <path d="M0 14 H228 Q236 14 240 6 Q244 0 252 0 H262 Q270 0 274 6 Q278 14 286 14 H330 V160 H0 Z" fill="#050505"/>
    </svg>
    <div class="wordmark">NURLO</div>
  </div>
</section>

</body>
</html>
```